Business Card

I need a business card that really pops for a potential customer or person who refers a personal injury lead. I want to highlight our office locations, but only address that needs to be on the card is my office's main address. I want a sleek, modern and minimalist design.

```html
<!DOCTYPE html>
<html lang="en">
<head>
<meta charset="utf-8">
<title>Lakeland Injury Lawyers – Business Card</title>
<link rel="stylesheet" href="https://fonts.googleapis.com/css2?family=Mulish:wght@400&display=swap">
<style>
  :root {
    --backdrop: #999999;
    --card-front: #000000;
    --card-back: #ffffff;
    --name-on-dark: #444444;
    --ink: #333333;
    --rule: #555555;
    --icon: #a8a8a8;
  }
  * { margin: 0; padding: 0; box-sizing: border-box; }
  html, body {
    width: 1200px; height: 1200px; overflow: hidden;
    background: var(--backdrop);
    font-family: "Mulish", sans-serif;
  }
  .canvas { position: relative; width: 1200px; height: 1200px; }
  .card {
    position: absolute; left: 201px; width: 797px; height: 464px;
    border-radius: 38px; overflow: hidden;
  }
  .card--front { top: 88px; background: var(--card-front); }
  .card--back { top: 613px; background: var(--card-back); }
  .firm-name {
    position: absolute; font-weight: 400; line-height: 1; white-space: nowrap;
    text-align: center;
  }
  .card--front .firm-name {
    left: 0; width: 100%; top: 211px;
    font-size: 40px; color: var(--name-on-dark);
  }
  .card--back .firm-name {
    left: 60px; width: 300px; top: 224px;
    font-size: 24px; color: var(--ink);
  }
  .divider {
    position: absolute; left: 383px; top: 183px; width: 1.5px; height: 103px;
    background: var(--rule);
  }
  .contact-list { position: absolute; left: 409px; top: 189px; list-style: none; }
  .contact-item {
    display: flex; align-items: center; height: 30.5px;
    font-size: 19.5px; color: var(--ink); letter-spacing: 0.1px;
  }
  .contact-item svg { width: 26px; height: 26px; margin-right: 10px; flex: none; }
  .icon { fill: none; stroke: var(--icon); stroke-width: 1.4; stroke-linecap: round; stroke-linejoin: round; }
  .address {
    position: absolute; left: 0; width: 100%; top: 388px;
    display: flex; justify-content: center; align-items: center;
    font-size: 19.5px; color: var(--ink);
  }
  .address svg { width: 30px; height: 36px; margin-right: 8px; }
</style>
</head>
<body>
<main class="canvas">
  <section class="card card--front" aria-label="Card front">
    <p class="firm-name">Lakeland Injury Lawyers</p>
  </section>

  <section class="card card--back" aria-label="Card back">
    <p class="firm-name">Lakeland Injury Lawyers</p>

    <div class="divider"></div>

    <ul class="contact-list">
      <li class="contact-item">
        <svg viewBox="0 0 26 26" aria-hidden="true"><path class="icon" d="M6 3.5l3.5 0 2 5-2.5 2a13 13 0 0 0 6.5 6.5l2-2.5 5 2v3.5a2 2 0 0 1-2 2A18 18 0 0 1 4 5.5a2 2 0 0 1 2-2z"/></svg>
        (312) 555-0148
      </li>
      <li class="contact-item">
        <svg viewBox="0 0 26 26" aria-hidden="true"><rect class="icon" x="2.5" y="6.5" width="21" height="14"/><path class="icon" d="M2.5 6.5l10.5 8.5 10.5-8.5M2.5 20.5l8-7M23.5 20.5l-8-7"/></svg>
        info@lakelandinjurylawyers.com
      </li>
      <li class="contact-item">
        <svg viewBox="0 0 26 26" aria-hidden="true"><circle class="icon" cx="13" cy="13" r="10"/><ellipse class="icon" cx="13" cy="13" rx="4.5" ry="10"/><path class="icon" d="M3 13h20M4.5 8h17M4.5 18h17M13 3v20"/></svg>
        lakelandinjurylawyers.com
      </li>
    </ul>

    <p class="address">
      <svg viewBox="0 0 30 36" aria-hidden="true"><path class="icon" d="M15 34C9 26 3.5 20 3.5 13a11.5 11.5 0 0 1 23 0C26.5 20 21 26 15 34z"/><circle class="icon" cx="15" cy="13" r="4.5"/></svg>
      210 West Harbor Street, Suite 1800, Chicago, IL 60601
    </p>
  </section>
</main>
</body>
</html>
```